添付は昨年のフォーマットです。
悪くはないのですが製本してパンフレットになると文字サイズなどのバランスが悪く・・・。
今年のフォーマットをお願いしたい。
添付のフォーマットの情報を網羅してデザイン願います。
• イラストレーター形式 (.ai)

ご提案ありがとうございました!
フォーマット原稿の性質上、シンプルで流し込みしやすいデザインを選ばせてもらいました。

皆様、ご提案ありがとうございました!
どれを選んでも問題ないフォーマットでした。
今後もまた提案よろしくお願いします。

```html
<!DOCTYPE html>
<html lang="ja">
<head>
<meta charset="utf-8">
<title>北嶺学園大学 学校案内</title>
<link href="https://fonts.googleapis.com/css2?family=Noto+Sans+JP:wght@400;500;700;900&family=Noto+Serif+JP:wght@700;900&display=swap" rel="stylesheet">
<style>
:root{
  --teal:#2b9ea6;
  --teal-pale:#e3f2f3;
  --navy:#1e2b55;
  --ink:#333;
  --grey:#8a8a8a;
  --panel:#d9d9d9;
  --rule:#c9c9c9;
  --dark:#3a3a3a;
  --accent:#c8202f;
}
*{box-sizing:border-box;margin:0;padding:0}
html,body{width:849px;height:1200px;overflow:hidden;background:#fff}
body{font-family:"Noto Sans JP",sans-serif;color:var(--ink);position:relative}
.page{position:absolute;inset:0}

.tab{position:absolute;left:22px;top:0;height:24px;display:flex;font-size:12px;font-weight:700}
.tab .no{background:var(--dark);color:#fff;padding:0 12px;line-height:24px}
.tab .pref{background:var(--teal);color:#fff;padding:0 16px;line-height:24px}

.title{position:absolute;left:26px;top:34px;display:flex;align-items:center;gap:12px;height:50px}
.title .mark{width:34px;height:34px;border-radius:50%;background:var(--accent)}
.title h1{font-family:"Noto Serif JP",serif;font-weight:900;font-size:42px;line-height:50px;letter-spacing:4px;color:var(--navy)}

.depts{position:absolute;left:28px;top:88px;width:500px;display:grid;grid-template-columns:repeat(3,1fr);row-gap:3px;font-size:11.5px;line-height:17px;color:var(--ink)}
.depts li{list-style:none;display:flex;align-items:center;gap:5px}
.depts li::before{content:"";width:8px;height:8px;background:var(--teal)}

.features{position:absolute;left:26px;top:150px;width:500px}
.features .label{display:inline-block;background:var(--teal);color:#fff;font-size:12px;line-height:16px;font-weight:700;padding:2px 10px}
.features .label b{color:#fff4a0}
.features ol{list-style:none;margin-top:6px;border-left:3px solid var(--teal)}
.features li{display:flex;align-items:center;gap:10px;font-size:19px;line-height:26px;font-weight:900;color:var(--navy);padding:2px 0 2px 8px;border-bottom:1px dotted var(--rule)}
.features li .num{width:24px;height:24px;background:var(--teal);color:#fff;font-size:15px;display:flex;align-items:center;justify-content:center}
.features li small{font-size:11px;font-weight:500;color:var(--ink)}

.visual{position:absolute;left:552px;top:68px;width:270px;height:188px;background:var(--panel);display:flex;flex-direction:column;align-items:center;justify-content:center;color:#fff;font-size:14px;font-weight:500}
.visual small{font-size:10px}

.guide-head{position:absolute;left:26px;top:292px;width:797px;display:flex;align-items:center;gap:14px;font-size:14px;font-weight:700;letter-spacing:6px;color:var(--navy)}
.guide-head::before,.guide-head::after{content:"";flex:1;height:1px;background:var(--rule)}

.section{position:absolute;width:386px}
.section .head{display:flex;align-items:center;gap:10px;padding-bottom:6px;border-bottom:2px solid var(--teal)}
.section .icon{width:34px;height:34px;background:var(--teal);display:flex;align-items:center;justify-content:center}
.section h2{font-size:22px;font-weight:900;color:var(--navy)}
.section p{margin-top:10px;font-size:11.5px;line-height:1.85;text-align:justify}
.section p .cap{float:left;font-family:"Noto Serif JP",serif;font-size:52px;line-height:1;font-weight:900;color:var(--navy);margin:2px 8px 0 0}
.s1{left:26px;top:322px}
.s2{left:437px;top:322px}
.s3{left:26px;top:560px}
.s4{left:437px;top:560px}

.okinawa{position:absolute;left:22px;top:990px;width:805px;height:78px;display:flex;border-top:1px solid var(--rule);border-bottom:1px solid var(--rule);align-items:center}
.okinawa .lab{width:160px;height:62px;background:var(--teal-pale);border-left:4px solid var(--teal);font-size:14px;font-weight:900;color:var(--navy);padding:8px 10px;line-height:1.35}
.okinawa ul{flex:1;list-style:none;display:flex;flex-wrap:wrap;gap:4px 14px;padding-left:16px;font-size:12px}

.footer{position:absolute;left:22px;top:1082px;width:805px;height:84px;display:flex;gap:10px}
.footer .msg-lab{width:92px;background:var(--teal);color:#fff;font-size:10px;font-weight:700;padding:6px;line-height:1.4;display:flex;flex-direction:column;gap:4px}
.footer .msg-lab .face{flex:1;background:rgba(255,255,255,.35)}
.footer .msg{flex:1;font-size:10.5px;line-height:1.6;padding-top:4px}
.footer .contact{width:260px;border:1px solid var(--teal);display:flex;flex-direction:column}
.footer .contact .cl{background:var(--teal);color:#fff;font-size:11px;font-weight:700;text-align:center;padding:2px}
.footer .contact .cb{font-size:10.5px;padding:6px 8px;line-height:1.6}
.footer .contact .cb strong{font-size:12px}
</style>
</head>
<body>
<div class="page">
  <div class="tab"><span class="no">School No.00</span><span class="pref">青森県</span></div>

  <div class="title"><span class="mark"></span><h1>北嶺学園大学</h1></div>

  <ul class="depts">
    <li>○○学部／○○学科</li><li>○○学部／○○学科</li><li>○○学部／○○学科</li>
    <li>○○学部／○○学科</li><li>○○学部／○○学科</li><li>○○学部／○○学科</li>
    <li>○○学部／○○学科</li><li>○○学部／○○学科</li><li>○○学部／○○学科</li>
  </ul>

  <div class="features">
    <span class="label"><b>ココに注目</b> 当校の特徴・魅力</span>
    <ol>
      <li><span class="num">1</span>学力優秀者奨学金制度あり</li>
      <li><span class="num">2</span>教員採用試験 123名合格<small>(昨年度合格)</small></li>
      <li><span class="num">3</span>管理栄養士合格率96.5%!</li>
    </ol>
  </div>

  <div class="visual" role="img" aria-label="大学キャンパスの写真スペース">フリービジュアルスペース<small>(W176×H86mm)</small></div>

  <div class="guide-head">学校案内</div>

  <section class="section s1">
    <div class="head"><span class="icon"><svg width="20" height="20" viewBox="0 0 20 20"><path d="M2 4h7v12H2zM11 4h7v12h-7z" fill="#fff"/></svg></span><h2>学びについて</h2></div>
    <p><span class="cap">本</span>学では、「共生」の精神のもと、学生一人ひとりの人間力を伸ばし社会に貢献できる人材を育成しています。専門的な知識と技能を身につけるだけでなく、地域や社会と関わる実践的な学びを重視し、少人数教育によるきめ細かな指導を行っています。実習や演習を通して課題を発見し解決する力を養い、卒業後も学び続ける姿勢を育てます。</p>
  </section>

  <section class="section s2">
    <div class="head"><span class="icon"><svg width="20" height="20" viewBox="0 0 20 20"><circle cx="10" cy="8" r="6" fill="#fff"/><rect x="9" y="12" width="2" height="6" fill="#fff"/></svg></span><h2>環境について</h2></div>
    <p><span class="cap">八</span>戸キャンパスは緑豊かな落ち着いた環境にあり、学業に集中できる施設が整っています。図書館や実習室、学生ラウンジなど多様な学びの場を用意し、授業の合間にも仲間と交流できます。通学バスや学生寮も完備し、県外出身の学生も安心して生活を始められます。</p>
  </section>

  <section class="section s3">
    <div class="head"><span class="icon"><svg width="20" height="20" viewBox="0 0 20 20"><circle cx="7" cy="7" r="3" fill="#fff"/><circle cx="14" cy="7" r="3" fill="#fff"/><path d="M1 18a6 6 0 0 1 12 0zM8 18a6 6 0 0 1 12 0z" fill="#fff"/></svg></span><h2>学生生活について</h2></div>
    <p><span class="cap">教</span>職員と学生の距離が近く、学習面から生活面まで担任制で丁寧にサポートしています。入学後すぐのオリエンテーションや新入生歓迎行事を通して、早い段階で友人をつくることができます。体育会やサークル活動も盛んで、多くの学生が学業と両立しながら活動しています。大学祭や地域のお祭りへの参加など、学外で活躍する機会も豊富です。</p>
    <p>また、奨学金制度や授業料減免制度を設け、経済面でも学生を支援しています。学生相談室では専門のカウンセラーが悩みに寄り添い、充実した四年間を過ごせるよう見守っています。留学や海外研修のプログラムも用意し、広い視野を持つ学生を育てています。</p>
  </section>

  <section class="section s4">
    <div class="head"><span class="icon"><svg width="20" height="20" viewBox="0 0 20 20"><rect x="2" y="6" width="16" height="11" fill="#fff"/><rect x="7" y="3" width="6" height="4" fill="none" stroke="#fff" stroke-width="2"/></svg></span><h2>就職支援について</h2></div>
    <p><span class="cap">八</span>戸・青森キャンパスにキャリア支援センターを設置し、1年次から段階的なキャリア教育を行っています。自己分析や業界研究、面接対策講座などを通して、一人ひとりの希望に合わせた進路選択を支援します。企業や自治体との連携によるインターンシップも充実しています。</p>
    <p>教員採用試験や国家試験に向けた対策講座も開講し、毎年高い合格実績を上げています。卒業生とのつながりを活かした就職相談会も好評で、多くの学生が希望の職に就いています。</p>
  </section>

  <div class="okinawa">
    <div class="lab">沖縄県出身在籍者の<br>高校別内訳</div>
    <ul>
      <li>糸満：5名</li><li>浦添：3名</li><li>那覇：4名</li><li>首里：1名</li><li>宜野湾：2名</li><li>読谷：1名</li>
      <li>名護：2名</li><li>石川：1名</li><li>北谷：3名</li><li>与那原：1名</li><li>コザ：1名</li><li>普天間：1名</li>
    </ul>
  </div>

  <div class="footer">
    <div class="msg-lab">大学担当者からのメッセージ<span class="face" role="img" aria-label="担当者の写真スペース"></span>入試広報課 担当</div>
    <p class="msg">沖縄県からも多くの学生が入学し、元気に学んでいます。オープンキャンパスや個別相談も随時受け付けていますので、お気軽にお問い合わせください。皆さんとキャンパスでお会いできることを楽しみにしています。</p>
    <div class="contact">
      <div class="cl">お問合わせ先</div>
      <div class="cb">〒000-0000 東京都中央区○○町3丁目120番地<br><strong>入試広報課 TEL:000-111-2222</strong></div>
    </div>
  </div>
</div>
</body>
</html>
```